Maplerise Trading Inc. needs an innovative idea for letterhead and visiting cards.

Maplerise Trading Inc. is a Canadian brand since 2007. It is a renown dealer of kids and office furniture locally. Moreover, exporting electric fixtures e.g. switches, LED's, down-lights etc. to Middle East and Africa. We have initiated a number of steps including re-branding, to boost our export in 2020. We have successfully designed our new logo a few months ago through 'Artfolio' and now we are looking for an innovative idea for a letterhead.
Some key points:
• Red, black and white are the three colors used in all our packaging and furniture. (grey is optional)
• Shouldn’t be too wide.
• Use of watermark is preferable.
• You can visit our North American site at www.mapleriseinc.com. Export website of the company will be launched soon. www.mapleriseinc.ca
• Same letterhead will be used locally and internationally.
• Our new logo and sample packaging is attached.

```html
<!DOCTYPE html>
<html lang="en">
<head>
<meta charset="utf-8">
<title>Maplerise Trading Inc. – Letterhead</title>
<link rel="stylesheet" href="https://fonts.googleapis.com/css2?family=Lato:wght@400;700&display=swap">
<style>
  :root {
    --brand-red: #9c1c22;
    --brand-grey: #474d50;
    --ink: #1e1e1e;
    --paper: #ffffff;
    --watermark: #ebd0c5;
  }
  html, body {
    margin: 0;
    padding: 0;
    overflow: hidden;
    background: var(--paper);
  }
  .letterhead {
    position: relative;
    width: 927px;
    height: 1200px;
    overflow: hidden;
    background: var(--paper);
    font-family: "Lato", sans-serif;
  }
  .header-wave {
    position: absolute;
    top: 0;
    left: 0;
    width: 927px;
    height: 80px;
  }
  .brand {
    position: absolute;
    left: 67px;
    top: 60px;
    display: flex;
    align-items: center;
    gap: 12px;
  }
  .brand-square {
    width: 58px;
    height: 58px;
    background: var(--brand-red);
    border-radius: 6px;
  }
  .brand-name {
    color: var(--brand-grey);
    font-weight: 700;
    font-size: 28px;
    line-height: 30px;
    letter-spacing: 1.5px;
    text-transform: uppercase;
  }
  .contact {
    position: absolute;
    left: 742px;
    top: 84px;
    font-size: 12.5px;
    color: var(--ink);
  }
  .contact-address {
    color: var(--brand-red);
    line-height: 15px;
    margin: 0 0 7px;
  }
  .contact-line {
    display: flex;
    align-items: center;
    gap: 6px;
    height: 20px;
    margin-bottom: 2px;
  }
  .contact-line svg {
    width: 14px;
    height: 14px;
    flex: none;
  }
  .watermark {
    position: absolute;
    left: 0;
    top: 520px;
    width: 867px;
    text-align: center;
    color: var(--watermark);
    font-weight: 700;
    font-size: 64px;
    line-height: 80px;
    letter-spacing: 3px;
    text-transform: uppercase;
  }
</style>
</head>
<body>
<main class="letterhead">
  <svg class="header-wave" viewBox="0 0 1500 130" preserveAspectRatio="none" aria-hidden="true">
    <path d="M0,0 H340 C210,20 90,60 0,115 Z" fill="var(--brand-red)"/>
    <path d="M680,0 H1500 V102 C1300,96 1050,60 680,0 Z" fill="var(--brand-red)"/>
    <path d="M235,36 C420,0 620,-4 820,22 S1220,108 1500,122" fill="none" stroke="var(--brand-grey)" stroke-width="11"/>
  </svg>

  <header class="brand">
    <div class="brand-square"></div>
    <div class="brand-name">Maplerise<br>Trading</div>
  </header>

  <address class="contact" style="font-style:normal">
    <p class="contact-address">248 Alder Cove Rd, Unit 305,<br>Thornbury,ON L3K 4P9</p>
    <div class="contact-line">
      <svg viewBox="0 0 16 16" aria-hidden="true"><circle cx="8" cy="8" r="7" fill="none" stroke="var(--brand-grey)" stroke-width="1.2"/><path d="M5.3,4.2 L6.6,5.6 L5.9,6.6 C6.5,7.9 7.6,9 8.9,9.6 L9.9,8.9 L11.3,10.2 L10.4,11.5 C7.4,11.1 4.9,8.6 4.4,5.2 Z" fill="var(--brand-grey)"/></svg>
      <span>+1 (800) 555-0147</span>
    </div>
    <div class="contact-line">
      <svg viewBox="0 0 16 16" aria-hidden="true"><rect x="1" y="3.5" width="14" height="9" fill="none" stroke="var(--brand-grey)" stroke-width="1"/><path d="M1,3.5 L8,9 L15,3.5 M1,12.5 L6,7.5 M15,12.5 L10,7.5" fill="none" stroke="var(--brand-grey)" stroke-width="1"/></svg>
      <span>info@mapleriseinc.com</span>
    </div>
    <div class="contact-line">
      <svg viewBox="0 0 16 16" aria-hidden="true"><circle cx="8" cy="8" r="7" fill="var(--brand-grey)"/><rect x="1" y="6.3" width="14" height="3.4" fill="var(--paper)"/><path d="M8,1 V15" stroke="var(--paper)" stroke-width="0.8"/></svg>
      <span>www.mapleriseinc.ca</span>
    </div>
  </address>

  <div class="watermark" aria-hidden="true">Maplerise<br>Trading</div>
</main>
</body>
</html>
```